Bookcover: Lessons From the Silent Orchard

I am publishing a super-low-cost innovation book for €4,99 on Bravolo Self Release to help everyone become a great innovator: young ambitious people without college education nor a big budget. Do you want to help me?

Brief:
Design a book cover 1600 x 2560 pixels for BSR.
Main title: Lessons From the Silent Orchard
Sub title: mindset - insights - skills & tools
Author: Maarten de Klerk
Design: captive, and appealing to everyone
Target Group: young ambitious people without college education

For bravolo please format the height/width ratio of 1.6:1

```html
<!DOCTYPE html>
<html lang="en">
<head>
<meta charset="utf-8">
<title>Lessons From the Silent Orchard — Maarten de Klerk</title>
<link rel="stylesheet" href="https://fonts.googleapis.com/css2?family=Bebas+Neue&family=Oswald:wght@200&display=swap">
<style>
  :root {
    --cover-orange: #ff8c00;
    --ink-black: #000000;
    --band-dark: #221f1f;
    --author-white: #ffffff;
    --bulb-yellow: #f6dc4a;
    --bulb-light: #fbe98a;
  }
  html, body {
    margin: 0;
    padding: 0;
    width: 800px;
    height: 1200px;
    overflow: hidden;
    background: var(--cover-orange);
  }
  .book-cover {
    display: block;
    width: 800px;
    height: 1200px;
  }
  .cover-ground { fill: var(--cover-orange); }
  .title-line {
    font-family: "Bebas Neue", "Oswald", sans-serif;
    fill: var(--ink-black);
  }
  .subtitle-line {
    font-family: "Oswald", sans-serif;
    font-weight: 200;
    fill: var(--ink-black);
  }
  .author-band { fill: var(--band-dark); }
  .author-name {
    font-family: "Bebas Neue", "Oswald", sans-serif;
    fill: var(--author-white);
    letter-spacing: 1px;
  }
</style>
</head>
<body>
<svg class="book-cover" viewBox="0 0 800 1200" xmlns="http://www.w3.org/2000/svg">
  <defs>
    <radialGradient id="bulbGlow" cx="50%" cy="40%" r="55%">
      <stop offset="0%" stop-color="var(--bulb-light)"/>
      <stop offset="70%" stop-color="var(--bulb-yellow)"/>
      <stop offset="100%" stop-color="var(--cover-orange)"/>
    </radialGradient>
  </defs>

  <rect class="cover-ground" x="0" y="0" width="800" height="1048"/>

  <g class="cover-title">
    <text class="title-line" x="40" y="204" font-size="204">LESSONS</text>
    <text class="title-line" x="40" y="363" font-size="204">FROM THE</text>
    <text class="title-line" x="40" y="581" font-size="262">SILENT</text>
    <text class="title-line" x="40" y="753" font-size="207">ORCHARD</text>
  </g>

  <rect class="idea-illustration" role="img"
        aria-label="Illustration of a crumpled yellow paper light bulb with radiating light strokes"
        x="560" y="390" width="190" height="210" rx="90" fill="url(#bulbGlow)"/>

  <g class="cover-subtitle">
    <text class="subtitle-line" x="42" y="890" font-size="92" textLength="642" lengthAdjust="spacingAndGlyphs">MINDSET - INSIGHTS -</text>
    <text class="subtitle-line" x="42" y="987" font-size="92" textLength="478" lengthAdjust="spacingAndGlyphs">SKILLS &amp; TOOLS</text>
  </g>

  <rect class="author-band" x="0" y="1048" width="800" height="152"/>
  <text class="author-name" x="43" y="1148" font-size="73">MAARTEN DE KLERK</text>
</svg>
</body>
</html>
```